Design concept for BrightKestrel.com Support Page

We are about to launch a new support page for our www.brightkestrel.com service for photographers and visual artists. The service provides media management, cloud storage, promotional and secure distribution to our members.

The support page will include FAQs and video tutorials.

In particular we're looking for a header for this page that suggests the user is in the support area of our service - so perhaps an illustration that suggests support could look nice (perhaps repair man or doctor iconography). Something to give this area of our site a different look and something that looks both cool and friendly.

Currently the page looks distinctly sparse and undesigned (see attached screenshot) - something that could be remedied, we feel, by some subtle design enhancements that we can implement using CSS.

```html
<!DOCTYPE html>
<html lang="en">
<head>
<meta charset="utf-8">
<title>BrightKestrel Support</title>
<link href="https://fonts.googleapis.com/css2?family=Ubuntu:wght@300;400;500;700&display=swap" rel="stylesheet">
<style>
  :root {
    --ink: #3d3d3d;
    --text: #555555;
    --muted: #8a8a8a;
    --sun: #f7b500;
    --sun-light: #fde9a8;
    --orange: #f47a20;
    --slate: #616a73;
    --panel: #ececec;
    --field: #bdbdbd;
    --white: #ffffff;
    --black: #000000;
    --footer-link: #a9a9a9;
  }
  * { box-sizing: border-box; margin: 0; padding: 0; }
  html, body { width: 784px; height: 1200px; overflow: hidden; }
  body {
    position: relative;
    background: var(--white);
    font-family: "Ubuntu", Arial, sans-serif;
    color: var(--text);
  }

  /* Top bar */
  .topbar { position: absolute; left: 0; top: 0; width: 784px; height: 52px; background: var(--white); }
  .brand {
    position: absolute; left: 20px; top: 12px;
    display: flex; align-items: center; gap: 8px;
  }
  .brand-mark { width: 22px; height: 22px; border-radius: 50%; background: var(--sun); }
  .brand-name { font-size: 25px; font-weight: 500; color: #595959; letter-spacing: -0.3px; }
  .account {
    position: absolute; left: 662px; top: 16px; width: 104px; height: 22px;
    border: 1px solid #d6d6d6; border-radius: 2px; background: var(--white);
    display: flex; align-items: center; padding: 0 6px 0 4px; gap: 6px;
    font-family: Arial, sans-serif; font-size: 9.5px; color: #333;
  }
  .account-avatar { width: 16px; height: 14px; background: #6c6c6c; }
  .account-caret { margin-left: auto; font-size: 7px; color: #888; }

  /* Hero */
  .hero {
    position: absolute; left: 0; top: 52px; width: 784px; height: 278px;
    background: linear-gradient(180deg, #fffaf0 0%, #fde7a8 35%, #fbcf55 75%, #f9c233 100%);
  }
  .hero-badge {
    position: absolute; left: 340px; top: 52px; width: 100px; height: 100px;
    border-radius: 50%; border: 3px solid var(--white);
    display: flex; align-items: center; justify-content: center;
  }
  .hero-badge-inner {
    width: 88px; height: 88px; border-radius: 50%; background: var(--white);
    display: flex; align-items: center; justify-content: center;
  }
  .hero-kicker {
    position: absolute; left: 0; width: 784px; top: 161px; text-align: center;
    font-size: 19px; font-weight: 400; color: var(--white);
  }
  .hero-title {
    position: absolute; left: 0; width: 784px; top: 181px; text-align: center;
    font-size: 38px; font-weight: 300; color: var(--white); letter-spacing: -0.5px;
  }

  /* Section shared */
  .section-title {
    position: absolute; left: 0; width: 784px; text-align: center;
    font-size: 25px; font-weight: 700; color: var(--ink);
  }
  .section-lead {
    position: absolute; left: 132px; width: 520px; text-align: center;
    font-size: 11.5px; line-height: 14px; color: var(--text);
  }

  /* Tutorials */
  .tutorials { position: absolute; left: 0; top: 330px; width: 784px; height: 348px; background: var(--panel); }
  .tutorials .section-title { top: 42px; }
  .tutorials .section-lead { top: 79px; }
  .tutorial {
    position: absolute; top: 135px; width: 166px; height: 167px;
    display: flex; align-items: center; justify-content: center;
  }
  .tutorial-1 { left: 53px;  background: linear-gradient(135deg, #c9b79a, #8a6a4e 60%, #d9c9a9); }
  .tutorial-2 { left: 227px; background: linear-gradient(135deg, #3d5a4b, #8aa23a 50%, #2a3a6a); }
  .tutorial-3 { left: 402px; background: linear-gradient(180deg, #0f3d5e, #2f7fa0 60%, #8cc3d6); }
  .tutorial-4 { left: 576px; background: linear-gradient(180deg, #8fb8c8, #e9c98a 60%, #6b6b6b); }

  /* FAQ */
  .faq { position: absolute; left: 0; top: 678px; width: 784px; height: 406px; background: var(--white); }
  .faq .section-title { top: 36px; }
  .faq .section-lead { top: 72px; left: 122px; width: 540px; }
  .search { position: absolute; left: 259px; top: 114px; display: flex; }
  .search-field { width: 203px; height: 26px; background: var(--field); border: none; }
  .search-button {
    width: 69px; height: 26px; background: var(--orange); color: var(--white);
    border: none; font-family: "Ubuntu", sans-serif; font-size: 12px;
  }
  .faq-list { position: absolute; left: 70px; top: 176px; width: 648px; list-style: none; }
  .faq-item {
    height: 31px; margin-bottom: 1px; border-radius: 3px; background: var(--slate);
    display: flex; align-items: center; padding-left: 18px; gap: 14px;
    color: var(--white); font-size: 12px;
  }
  .faq-item.is-active { background: var(--sun); }
  .faq-toggle {
    width: 17px; height: 17px; border-radius: 50%; background: var(--white);
    color: var(--sun); font-size: 13px; font-weight: 700; line-height: 17px; text-align: center;
  }

  /* Footer */
  .footer { position: absolute; left: 0; top: 1084px; width: 784px; height: 116px; background: var(--black); text-align: center; }
  .footer-nav { position: absolute; top: 26px; width: 784px; font-size: 10.5px; color: var(--footer-link); }
  .footer-nav span.sep { margin: 0 6px; }
  .footer-copy { position: absolute; top: 60px; width: 784px; font-size: 10px; font-weight: 500; color: var(--white); }
  .footer-powered { position: absolute; top: 74px; width: 784px; font-size: 10px; color: #6f6f6f; }
</style>
</head>
<body>

<header class="topbar">
  <div class="brand">
    <span class="brand-mark"></span>
    <span class="brand-name">BrightKestrel</span>
  </div>
  <div class="account">
    <span class="account-avatar" role="img" aria-label="Member avatar"></span>
    <span>Marek Solis</span>
    <span class="account-caret">▼</span>
  </div>
</header>

<section class="hero" role="img" aria-label="Soft golden backdrop of a sunlit park scene">
  <div class="hero-badge">
    <div class="hero-badge-inner">
      <svg width="44" height="44" viewBox="0 0 44 44" aria-hidden="true">
        <path d="M9 24 V20 a13 13 0 0 1 26 0 V24" fill="none" stroke="#555" stroke-width="3"/>
        <rect x="6" y="21" width="7" height="12" rx="3" fill="#555"/>
        <rect x="31" y="21" width="7" height="12" rx="3" fill="#555"/>
        <path d="M34 33 q0 6 -9 6" fill="none" stroke="#555" stroke-width="2"/>
        <rect x="20" y="37" width="6" height="4" rx="2" fill="#555"/>
      </svg>
    </div>
  </div>
  <p class="hero-kicker">BrightKestrel Support</p>
  <h1 class="hero-title">We’re happy to help ...</h1>
</section>

<section class="tutorials">
  <h2 class="section-title">Video Tutorials</h2>
  <p class="section-lead">Lorem ipsum dolor sit amet, consectetur adipisicing elit, sed do eiusmod tempor incididunt ut labore et dolore magna aliqua. Ut enim ad minim veniam, quis nostrud exercitation ullamco laboris.</p>
  <div class="tutorial tutorial-1" role="img" aria-label="Tutorial still: camera on a strap">
    <svg width="60" height="60" viewBox="0 0 60 60" aria-hidden="true"><circle cx="30" cy="30" r="27" fill="rgba(255,255,255,0.12)" stroke="#fff" stroke-width="3" opacity=".85"/><path d="M24 18 L42 30 L24 42 Z" fill="#fff" opacity=".85"/></svg>
  </div>
  <div class="tutorial tutorial-2" role="img" aria-label="Tutorial still: hand with coloured powder">
    <svg width="60" height="60" viewBox="0 0 60 60" aria-hidden="true"><circle cx="30" cy="30" r="27" fill="rgba(255,255,255,0.12)" stroke="#fff" stroke-width="3" opacity=".85"/><path d="M24 18 L42 30 L24 42 Z" fill="#fff" opacity=".85"/></svg>
  </div>
  <div class="tutorial tutorial-3" role="img" aria-label="Tutorial still: macro shot of a dark object on beads">
    <svg width="60" height="60" viewBox="0 0 60 60" aria-hidden="true"><circle cx="30" cy="30" r="27" fill="rgba(255,255,255,0.12)" stroke="#fff" stroke-width="3" opacity=".85"/><path d="M24 18 L42 30 L24 42 Z" fill="#fff" opacity=".85"/></svg>
  </div>
  <div class="tutorial tutorial-4" role="img" aria-label="Tutorial still: photographer silhouetted above clouds">
    <svg width="60" height="60" viewBox="0 0 60 60" aria-hidden="true"><circle cx="30" cy="30" r="27" fill="rgba(255,255,255,0.12)" stroke="#fff" stroke-width="3" opacity=".85"/><path d="M24 18 L42 30 L24 42 Z" fill="#fff" opacity=".85"/></svg>
  </div>
</section>

<section class="faq">
  <h2 class="section-title">Frequently Asked Questions</h2>
  <p class="section-lead">Lorem ipsum dolor sit amet, consectetur adipisicing elit, sed do eiusmod tempor incididunt ut labore et dolore magna aliqua. Ut enim ad minim veniam, quis nostrud exercitation ullamco laboris.</p>
  <form class="search">
    <input class="search-field" type="text" aria-label="Search questions">
    <button class="search-button" type="button">search</button>
  </form>
  <ul class="faq-list">
    <li class="faq-item is-active"><span class="faq-toggle">+</span>Uploading Files Using the Drag and Drop Uploader</li>
    <li class="faq-item"><span class="faq-toggle">+</span>Publishing Files</li>
    <li class="faq-item"><span class="faq-toggle">+</span>Creating Galleries</li>
    <li class="faq-item"><span class="faq-toggle">+</span>Creating Portfolios</li>
    <li class="faq-item"><span class="faq-toggle">+</span>Re-ordering Files within Galleries of Portfolios</li>
    <li class="faq-item"><span class="faq-toggle">+</span>Managing Folder and Files</li>
  </ul>
</section>

<footer class="footer">
  <nav class="footer-nav">
    Home<span class="sep">·</span>Contact Us<span class="sep">·</span>Affiliate Program<span class="sep">·</span>Privacy Policy<span class="sep">·</span>Site Terms and Conditions<span class="sep">·</span>About Us
  </nav>
  <p class="footer-copy">© Copyright 2014 Harbourline Images Pte Ltd. All rights reserved.</p>
  <p class="footer-powered">Powered by BrightKestrel</p>
</footer>

</body>
</html>
```